VELMORA BRIDGE ADVISORY

Need a Boucher designed with vibrant colours and well aligned. The content is there in the word file what I have attached. The heading and the subject of each paragraph has to be separated by designing accordingly. I would appreciate if nice hd pictures of stock market/trading/forex/consulting can be accommodated with this.

Target Market(s)

traders, stock traders, business entrepreneurs

Font styles to use
Sans Serif

Requirements
Must have
• Images from stock market and charts
Nice to have
• I want it to look elegant as this goes to the trading community.
Should not have
• Don't want anything that looks goody or fashionable since its a professional broucher.

```html
<!DOCTYPE html>
<html lang="en">
<head>
<meta charset="utf-8">
<title>Trading a Serious Business – Velmora Bridge Advisory</title>
<link rel="stylesheet" href="https://fonts.googleapis.com/css2?family=Fira+Sans+Extra+Condensed:wght@500;600&family=Open+Sans:wght@700&display=swap">
<style>
  :root {
    --paper: #ffffff;
    --ink-grey: #666666;
    --accent-orange: #ff6a13;
    --accent-cyan: #00ade3;
    --sky-blue: #51a6d3;
    --deep-blue: #2f5b93;
    --night-blue: #34466f;
    --white: #ffffff;
  }
  * { margin: 0; padding: 0; box-sizing: border-box; }
  html, body { width: 945px; height: 1200px; overflow: hidden; background: var(--paper); }
  .cover {
    position: relative;
    width: 945px;
    height: 1200px;
    background: var(--paper);
    font-family: "Fira Sans Extra Condensed", "Arial Narrow", sans-serif;
  }
  .cover-art { position: absolute; inset: 0; width: 945px; height: 1200px; }
  .brand {
    position: absolute;
    left: 55px;
    top: 68px;
    display: flex;
    align-items: center;
    gap: 18px;
  }
  .brand-square { width: 70px; height: 70px; background: var(--ink-grey); }
  .brand-name {
    font-family: "Open Sans", sans-serif;
    font-weight: 700;
    font-size: 38px;
    letter-spacing: 2px;
    color: var(--ink-grey);
  }
  .year-tag {
    position: absolute;
    left: 753px;
    top: 0;
    width: 130px;
    height: 127px;
    background: var(--accent-cyan);
    display: flex;
    align-items: flex-end;
    justify-content: center;
    padding-bottom: 4px;
    font-family: "Open Sans", sans-serif;
    font-weight: 700;
    font-size: 40px;
    color: var(--white);
  }
  .title {
    position: absolute;
    left: 308px;
    top: 297px;
    width: 600px;
    font-weight: 500;
    font-size: 52px;
    line-height: 59px;
    color: var(--ink-grey);
  }
  .title-accent { color: var(--accent-orange); }
  .byline {
    position: absolute;
    right: 77px;
    top: 1064px;
    text-align: right;
    font-weight: 500;
    font-size: 24px;
    line-height: 29px;
    color: var(--white);
  }
  .byline-label { color: var(--accent-cyan); }
</style>
</head>
<body>
<main class="cover">
  <svg class="cover-art" viewBox="0 0 1312 1855" preserveAspectRatio="none" aria-hidden="false">
    <defs>
      <linearGradient id="trading-photo-tone" x1="0" y1="0" x2="0" y2="1">
        <stop offset="0" stop-color="#51a6d3"/>
        <stop offset="0.35" stop-color="#51a6d3"/>
        <stop offset="0.6" stop-color="#3f85c8"/>
        <stop offset="0.85" stop-color="#2f5b93"/>
        <stop offset="1" stop-color="#34466f"/>
      </linearGradient>
    </defs>
    <path class="grey-panel" fill="#666666"
      d="M1312,820 C1240,820 1190,850 1150,890 L775,1258 L480,1855 L1312,1855 Z"/>
    <path class="orange-band" fill="#ff6a13"
      d="M775,1258 Q870,1350 832,1480 Q812,1535 770,1575 L478,1855 L272,1855 Q274,1790 345,1718 Z"/>
    <path class="trading-photo" fill="url(#trading-photo-tone)" role="img"
      aria-label="Photo of hands using a tablet with glowing currency symbols, forex trading text and market charts over a world map"
      d="M0,483 L775,1258 L345,1718 Q274,1790 272,1855 L0,1855 Z"/>
  </svg>

  <div class="brand">
    <span class="brand-square"></span>
    <span class="brand-name">VELMORA</span>
  </div>

  <div class="year-tag">2020</div>

  <h1 class="title"><span class="title-accent">“Trading”</span> a Serious Business, Importance of Capital and The Rise in Proprietary Trading Firm</h1>

  <p class="byline">
    <span class="byline-label">BY</span><br>
    VELMORA BRIDGE ADVISORY<br>
    DEVAN MIRALKAR
  </p>
</main>
</body>
</html>
```